Business Card Design Project

I am seeking a business card for my life coaching career. I specialize in coaching executives and entrepreneurs. Consciousness plays a key role in my practice.
Updates

I would like to see different fonts -I don't like the way the capital J looks. I only want my name once on the card, on the front. I like everything centered on the front, with a white background, grey and green on the front; and the same grey on the back with bullet points next to each quality; centered. I like a subtle shadow of the mountains behind the text on the back of the card. I don't want the mountains on either side to be too big. Thank you.

Target Market(s)

Middle age business owners/executives

Industry/Entity Type

Business

Contact Information for Business Card

The front design is my name and a mountain logo. I want to have my name prominently shown.

Requirements
Must have
• Front of card:
• My name prominent sized font
• Helping clients lead more fulfilling lives;
• Executive Life Coach
• 555-304-7781
• rkovet4@mailbriar.com
• Back of Card:
• Providing Unparalleled support
• Providing a safe place to grow in self-awareness
• 20+ years entrepreneurial experience
• Trust
• Integrity
Nice to have
• Easy to read font; warm colors reflecting a masculine personality.

Files

```html
<!DOCTYPE html>
<html lang="en">
<head>
<meta charset="utf-8">
<title>Reid Halvorsen – Business Card</title>
<link rel="stylesheet" href="https://fonts.googleapis.com/css2?family=Open+Sans:wght@400;600;700&family=EB+Garamond:wght@400&display=swap">
<style>
  :root {
    --page-bg: #ecebe8;
    --card-white: #ffffff;
    --card-grey: #58585a;
    --brand-green: #4e6b3a;
    --text-grey: #555555;
    --text-light: #f2f2f2;
    --shadow: rgba(0, 0, 0, 0.18);
  }
  * { box-sizing: border-box; margin: 0; padding: 0; }
  html, body {
    width: 1200px;
    height: 891px;
    overflow: hidden;
    background: var(--page-bg);
  }
  .canvas {
    position: relative;
    width: 1200px;
    height: 891px;
    display: flex;
    align-items: center;
    justify-content: center;
    gap: 60px;
  }
  .card {
    position: relative;
    width: 510px;
    height: 292px;
    box-shadow: 0 6px 18px var(--shadow);
  }
  .card-front {
    background: var(--card-white);
    font-family: "Open Sans", Arial, sans-serif;
    color: var(--text-grey);
  }
  .brand {
    position: absolute;
    top: 52px;
    left: 150px;
    display: flex;
    align-items: center;
    gap: 14px;
  }
  .brand-mark {
    width: 14px;
    height: 14px;
    background: var(--brand-green);
  }
  .brand-name {
    font-size: 38px;
    font-weight: 700;
    color: var(--brand-green);
    line-height: 1;
    letter-spacing: 0.5px;
  }
  .brand-title {
    position: absolute;
    top: 100px;
    left: 178px;
    font-size: 15px;
    font-weight: 600;
    color: var(--brand-green);
  }
  .contact {
    position: absolute;
    left: 60px;
    top: 150px;
    display: flex;
    flex-direction: column;
    gap: 10px;
  }
  .tagline {
    font-size: 17px;
    font-weight: 600;
    letter-spacing: 0.6px;
  }
  .contact-line {
    font-size: 18px;
    font-weight: 700;
    padding-left: 52px;
    letter-spacing: 0.4px;
  }
  .card-back {
    background: var(--card-grey);
    font-family: "EB Garamond", Georgia, serif;
    color: var(--text-light);
    display: flex;
    align-items: center;
    justify-content: center;
  }
  .qualities {
    list-style: none;
    font-size: 15.5px;
    line-height: 1.3;
  }
  .qualities li::before {
    content: "•";
    margin-right: 6px;
  }
</style>
</head>
<body>
  <main class="canvas">
    <section class="card card-front" aria-label="Business card front">
      <div class="brand">
        <span class="brand-name">Reid Halvorsen</span>
        <span class="brand-mark" aria-hidden="true"></span>
      </div>
      <p class="brand-title">Executive Live Coach</p>
      <div class="contact">
        <p class="tagline">Helping Clients Lead More Fulfilling Lives</p>
        <p class="contact-line">rkovet4@mailbriar.com</p>
        <p class="contact-line">555-304-7781</p>
      </div>
    </section>

    <section class="card card-back" aria-label="Business card back">
      <ul class="qualities">
        <li>Trust</li>
        <li>Integrity</li>
        <li>Integrating consciousness into your life</li>
        <li>Unparalled support</li>
        <li>Providing a safe place to grow in self-awareness</li>
        <li>20+ years entrepreneurial experience</li>
      </ul>
    </section>
  </main>
</body>
</html>
```